Lobby Sentinel Staffing

Lobby sentinel is similar to a security company but is more concierge/customer service oriented. Picture a security guard in a suit working at a condo or office building. Our thoughts for a logo is a silhouette of a male/female sitting at a desk or some type of crest but were open to creative ideas.

Target Market(s)

Property Managers

Industry/Entity Type

Security

Font styles to use
Serif

Requirements
Must have
• Male/Female sitting professionally at a desk.
Nice to have
• Vertical card
Should not have
• Cartoons

```html
<!DOCTYPE html>
<html lang="en">
<head>
<meta charset="utf-8">
<title>Lobby Sentinel Staffing – Business Card</title>
<link href="https://fonts.googleapis.com/css2?family=Noto+Sans:ital,wght@0,400;0,700;1,400&display=swap" rel="stylesheet">
<style>
  :root{
    --stage-light:#ececec;
    --stage-dark:#4b4746;
    --navy:#2f3190;
    --navy-deep:#14153f;
    --ink:#050510;
    --band:#1c1c1e;
    --lavender:#c9c9e6;
    --white:#ffffff;
    --text-dark:#111111;
  }
  *{margin:0;padding:0;box-sizing:border-box}
  html,body{width:1200px;height:1158px;overflow:hidden}
  body{
    position:relative;
    background:linear-gradient(135deg,var(--stage-light) 0%,#a9a9a9 50%,var(--stage-dark) 100%);
    font-family:"Noto Sans",sans-serif;
  }
  .card{
    position:absolute;
    top:246px;
    width:516px;height:665px;
    border-radius:20px;
    overflow:hidden;
  }
  .card-art{position:absolute;inset:0;width:100%;height:100%;display:block}
  .card--front{left:72px;background:var(--ink)}
  .card--back{left:612px;background:var(--white)}

  .brand-name{
    position:absolute;
    color:var(--white);
    font-weight:400;
    white-space:nowrap;
    letter-spacing:0.3px;
  }
  .card--front .brand-name{right:30px;top:680px;top:432px;font-size:29px}
  .card--back .brand-name{left:0;right:0;top:62px;text-align:center;font-size:30px}

  .holder{position:absolute;left:23px;top:322px;color:var(--text-dark)}
  .holder-name{font-size:28px;font-weight:700;line-height:1.2}
  .holder-title{font-size:23px;font-style:italic;line-height:1.3}

  .contact{
    position:absolute;left:248px;top:582px;
    list-style:none;
    font-size:15px;line-height:20px;color:var(--text-dark);
  }
</style>
</head>
<body>

<section class="card card--front">
  <svg class="card-art" viewBox="0 0 449 579" preserveAspectRatio="none">
    <defs>
      <linearGradient id="front-top" x1="0" y1="0" x2="1" y2="0">
        <stop offset="0" stop-color="#2f3190"/>
        <stop offset="0.55" stop-color="#2a2c84"/>
        <stop offset="1" stop-color="#070718"/>
      </linearGradient>
      <linearGradient id="front-base" x1="0" y1="0" x2="1" y2="0">
        <stop offset="0" stop-color="#020208"/>
        <stop offset="0.5" stop-color="#1d1e5e"/>
        <stop offset="1" stop-color="#2f3190"/>
      </linearGradient>
      <linearGradient id="front-fade" x1="0" y1="0" x2="0" y2="1">
        <stop offset="0" stop-color="#fff"/>
        <stop offset="0.15" stop-color="#fff"/>
        <stop offset="0.3" stop-color="#000"/>
      </linearGradient>
      <mask id="top-fade"><rect width="449" height="579" fill="url(#front-fade)"/></mask>
      <linearGradient id="figure-tone" x1="0" y1="0" x2="1" y2="1">
        <stop offset="0" stop-color="#ffffff" stop-opacity="0.85"/>
        <stop offset="1" stop-color="#dcdcf0" stop-opacity="0.6"/>
      </linearGradient>
    </defs>
    <rect width="449" height="579" fill="url(#front-base)"/>
    <rect width="449" height="579" fill="url(#front-top)" mask="url(#top-fade)"/>
    <ellipse cx="140" cy="310" rx="260" ry="225" fill="#14153f" opacity="0.55"/>
    <ellipse cx="222" cy="292" rx="222" ry="200" transform="rotate(30 222 292)" fill="var(--navy)"/>
    <rect class="figure-area" x="45" y="124" width="385" height="236" rx="30" fill="url(#figure-tone)"
          role="img" aria-label="White silhouette of a receptionist with a headset seated at a desk with a computer monitor and keyboard"/>
  </svg>
  <p class="brand-name">Lobby Sentinel Staffing</p>
</section>

<section class="card card--back">
  <svg class="card-art" viewBox="0 0 449 579" preserveAspectRatio="none" aria-hidden="true">
    <defs>
      <linearGradient id="back-strip" x1="0" y1="0" x2="1" y2="0">
        <stop offset="0" stop-color="#f2f2fa"/>
        <stop offset="0.6" stop-color="#8586c2"/>
        <stop offset="1" stop-color="#2f3190"/>
      </linearGradient>
      <linearGradient id="back-band" x1="0" y1="0" x2="1" y2="0">
        <stop offset="0" stop-color="#2a2a2c"/>
        <stop offset="1" stop-color="#0c0c14"/>
      </linearGradient>
      <linearGradient id="back-wave" x1="0" y1="0" x2="1" y2="0">
        <stop offset="0" stop-color="#2f3190"/>
        <stop offset="0.55" stop-color="#7f80bf"/>
        <stop offset="1" stop-color="#2f3190"/>
      </linearGradient>
      <linearGradient id="back-sheen" x1="0" y1="0" x2="1" y2="1">
        <stop offset="0" stop-color="#ffffff" stop-opacity="0.9"/>
        <stop offset="1" stop-color="#c9c9e6"/>
      </linearGradient>
    </defs>
    <rect width="449" height="40" fill="url(#back-strip)"/>
    <rect y="108" width="449" height="300" fill="url(#back-wave)"/>
    <path d="M0,150 C150,90 330,130 449,285 L449,579 L0,579 Z" fill="url(#back-sheen)"/>
    <path d="M0,152 C160,120 330,175 449,352 L449,579 L0,579 Z" fill="var(--white)"/>
    <rect y="39" width="449" height="69" fill="url(#back-band)"/>
  </svg>
  <p class="brand-name">Lobby Sentinel Staffing</p>
  <div class="holder">
    <p class="holder-name">Your Name</p>
    <p class="holder-title">Job Title</p>
  </div>
  <ul class="contact">
    <li>Your Number</li>
    <li>Email : yourcompany@mail.com</li>
    <li>Website : www.yourcompany.com</li>
  </ul>
</section>

</body>
</html>
```